Finiding oppertunites in Real Estate 6.15.20

size of ad 7” x 9.6”
1-I like the ad to stand out and attract people's attention.
2-you should be able to see the text of the ad clearly .. see the attachment anything in yellow is instructions.
3-the list of topics should not be the main part of the ad
4-if you decide you want a picture or vector of a person .. (you decide)
then it should be a white male about 25-30 years old wearing a solid white or blue shirt and not long hair.
5-leave 1 inch for footer
see attachment
Good luck

Target Market(s)

potential male students 25-35 years of age

Industry/Entity Type

Education

Requirements
Must have
• will stand out and people would want to see it.
should be able to read the words of ad
Nice to have
• how to make money in real estate on one line

```html
<!DOCTYPE html>
<html lang="en">
<head>
<meta charset="utf-8">
<title>Real Estate Career Course</title>
<link href="https://fonts.googleapis.com/css2?family=Russo+One&family=Poppins:wght@400;500;600&family=Zilla+Slab:ital,wght@1,700&display=swap" rel="stylesheet">
<style>
  :root {
    --navy: #263c6c;
    --navy-deep: #262f5e;
    --blue: #1d6fb7;
    --sky: #7fd0f0;
    --teal: #5cbfc0;
    --ink: #2b2b2b;
    --paper: #f4f9fc;
    --white: #ffffff;
  }
  * { margin: 0; padding: 0; box-sizing: border-box; }
  html, body { width: 875px; height: 1200px; overflow: hidden; }
  body {
    font-family: "Poppins", sans-serif;
    color: var(--ink);
    background: var(--paper);
  }
  .ad {
    position: relative;
    width: 875px;
    height: 1200px;
    overflow: hidden;
    background: linear-gradient(180deg, #f7fbfd 0%, #eaf5fa 55%, #cfe9f3 100%);
  }
  .corner-wave { position: absolute; top: 0; right: 0; }
  .title {
    position: absolute;
    left: 0; width: 832px;
    text-align: center;
    font-family: "Russo One", sans-serif;
    line-height: 1;
  }
  .title-top { top: 48px; font-size: 50px; color: var(--blue); letter-spacing: 1px; }
  .title-bottom { top: 104px; font-size: 53px; color: var(--navy); letter-spacing: 0.5px; }

  .divider { position: absolute; top: 186px; width: 2px; height: 146px; background: var(--navy); }
  .divider-left { left: 214px; }
  .divider-right { left: 569px; }

  .pitch { position: absolute; font-size: 22px; line-height: 30px; letter-spacing: -0.6px; }
  .pitch strong { font-weight: 600; color: var(--blue); }
  .pitch-money { left: 38px; top: 207px; }
  .pitch-start { left: 226px; width: 340px; top: 204px; text-align: center; }
  .pitch-start .highlight {
    display: inline-block;
    margin-top: 2px;
    padding: 0 6px;
    background: var(--navy);
    color: var(--white);
    font-weight: 500;
    font-size: 24px;
    line-height: 35px;
  }
  .pitch-invest { right: 37px; top: 192px; text-align: right; }

  .hero-art {
    position: absolute; left: 150px; top: 318px;
    width: 520px; height: 460px;
  }
  .remote-badge { position: absolute; left: 138px; top: 326px; }

  .course-heading { position: absolute; left: 204px; top: 782px; font-family: "Russo One", sans-serif; color: var(--navy); }
  .course-number {
    position: absolute; left: 0; top: -6px;
    font-size: 100px; line-height: 1; letter-spacing: -7px;
    transform: scaleX(0.78); transform-origin: left top;
  }
  .course-sup { position: absolute; left: 64px; top: 3px; font-size: 14px; }
  .course-session { position: absolute; left: 81px; top: 9px; font-size: 40px; white-space: nowrap; line-height: 1; }
  .course-session span { color: var(--blue); margin-left: 14px; }
  .course-date { position: absolute; left: 86px; top: 55px; font-size: 24px; white-space: nowrap; line-height: 1; letter-spacing: 0.5px; }

  .topics-label {
    position: absolute; left: 286px; top: 886px;
    width: 288px; height: 32px;
    background: var(--blue);
    border-radius: 10px 16px 10px 16px;
    color: var(--white);
    font-size: 16.5px; font-weight: 600;
    text-align: center; line-height: 32px;
    box-shadow: 0 8px 6px -6px rgba(30,50,90,0.55);
  }
  .topic-list { position: absolute; list-style: none; }
  .topic-list li {
    position: relative;
    padding-left: 24px;
    height: 35.5px;
    font-size: 17.5px;
    line-height: 20px;
  }
  .topic-list li::before {
    content: "";
    position: absolute; left: 0; top: 3px;
    width: 13px; height: 13px;
    background: linear-gradient(45deg, var(--navy) 50%, var(--blue) 50%);
  }
  .topics-one { left: 74px; top: 947px; }
  .topics-two { left: 339px; top: 947px; }
  .topics-three { left: 635px; top: 947px; }

  .footer {
    position: absolute; left: 0; bottom: 0;
    width: 875px; height: 70px;
    background: var(--navy-deep);
    color: var(--white);
    font-size: 22px;
    text-align: center; line-height: 70px;
    letter-spacing: 0.2px;
  }
  .footer .sep { margin: 0 10px; }
</style>
</head>
<body>
<main class="ad">
  <svg class="corner-wave" width="190" height="200" viewBox="0 0 190 200">
    <defs>
      <linearGradient id="cornerGrad" x1="0" y1="0" x2="1" y2="1">
        <stop offset="0" stop-color="#4d5fae"/>
        <stop offset="1" stop-color="#5cc2c0"/>
      </linearGradient>
    </defs>
    <path d="M3 0 C40 40 110 60 147 72 C150 120 160 170 190 192 V0 Z" fill="url(#cornerGrad)"/>
  </svg>

  <h1>
    <span class="title title-top">REAL ESTATE</span>
    <span class="title title-bottom">CAREER COURSE</span>
  </h1>

  <div class="divider divider-left"></div>
  <div class="divider divider-right"></div>

  <p class="pitch pitch-money">How To Make<br><strong>Money In</strong><br>In Real Estate?</p>
  <p class="pitch pitch-start">For Those Who Have Started<br>Or Would Like To Go<br><span class="highlight">Into Real Estate</span></p>
  <p class="pitch pitch-invest">An Investment<br><strong>In Knowledge Opens</strong><br>Up Untold Opportunities</p>

  <svg class="hero-art" viewBox="0 0 520 460" role="img" aria-label="Illustration of a young real estate agent in a navy suit presenting a white house with trees, on a blue and teal backdrop">
    <defs>
      <linearGradient id="heroGrad" x1="0.1" y1="0" x2="0.8" y2="1">
        <stop offset="0" stop-color="#93dbf5"/>
        <stop offset="0.45" stop-color="#5cc3cf"/>
        <stop offset="1" stop-color="#4b5aa8"/>
      </linearGradient>
      <radialGradient id="heroShadow" cx="0.5" cy="0.5" r="0.5">
        <stop offset="0" stop-color="#8aa4b8" stop-opacity="0.45"/>
        <stop offset="1" stop-color="#8aa4b8" stop-opacity="0"/>
      </radialGradient>
    </defs>
    <ellipse cx="450" cy="300" rx="90" ry="60" fill="url(#heroShadow)"/>
    <path d="M60 150 C70 70 150 10 240 22 C320 32 360 20 420 60 C480 100 500 190 490 270 C478 350 420 410 320 412 C230 414 150 410 90 370 C40 330 50 230 60 150 Z" fill="url(#heroGrad)"/>
    <circle cx="384" cy="56" r="16" fill="#1d6fb7"/>
    <circle cx="470" cy="134" r="21" fill="#1d6fb7"/>
    <circle cx="224" cy="436" r="18" fill="#5ba6c0"/>
    <g stroke="#1d6fb7" stroke-width="2">
      <path d="M421 181 v10 M416 186 h10"/>
      <path d="M485 332 v10 M480 337 h10"/>
      <path d="M176 420 v10 M171 425 h10"/>
      <path d="M343 434 v10 M338 439 h10"/>
    </g>
  </svg>

  <svg class="remote-badge" width="160" height="180" viewBox="0 0 160 180">
    <polygon fill="#263c6c" points="80,6 92,34 118,18 118,48 150,46 134,72 158,92 128,104 140,134 108,128 104,162 82,140 60,168 54,134 24,146 32,116 4,100 30,82 12,56 44,52 40,22 66,36"/>
    <text x="83" y="72" text-anchor="middle" font-family="Zilla Slab, serif" font-style="italic" font-weight="700" font-size="25" fill="#ffffff">Remote</text>
    <text x="86" y="98" text-anchor="middle" font-family="Zilla Slab, serif" font-style="italic" font-weight="700" font-size="25" fill="#ffffff">Sessions</text>
  </svg>

  <section class="course-heading">
    <div class="course-number">12</div>
    <div class="course-sup">TH</div>
    <div class="course-session">SESSION<span>COURSE</span></div>
    <div class="course-date">CLASSES STARTING JUNE 16</div>
  </section>

  <div class="topics-label">A PARTIAL LISTING OF TOPICS</div>

  <ul class="topic-list topics-one">
    <li>Single-family</li>
    <li>Multifamily</li>
    <li>Management</li>
    <li>Real Estate Concepts</li>
    <li>HUD properties</li>
  </ul>
  <ul class="topic-list topics-two">
    <li>Real Estate law</li>
    <li>Investment properties</li>
    <li>Foreclosures</li>
    <li>Rehab</li>
    <li>Due Diligence e</li>
  </ul>
  <ul class="topic-list topics-three">
    <li>Foreclosures</li>
    <li>Short sales</li>
    <li>Development</li>
    <li>Finical modeling</li>
  </ul>

  <footer class="footer">
    0800 555 014<span class="sep">|</span>propertypathcourse.info<span class="sep">|</span>propertypathcourse.com
  </footer>
</main>
</body>
</html>
```